Brellow Gateworks garage door installation service and repairs

I need a business card design for my company that is called Brellow Gateworks, I install, service, repair and automate garaged doors.
I want my card to look simple and neat but I also want the information such as contact number, email address and website to be clear and noticeable. I would love a simple logo if possible, I would like to see the color blue in the card but not overpowering.

Industry/Entity Type

Garage

```html
<!DOCTYPE html>
<html lang="en">
<head>
<meta charset="utf-8">
<title>Brellow Gateworks – Business Card</title>
<link rel="stylesheet" href="https://fonts.googleapis.com/css2?family=Archivo+Black&family=Cousine:ital,wght@1,700&display=swap">
<style>
  :root {
    --backdrop: #e7e4df;
    --blue-deep: #4a4ed4;
    --blue-soft: #7474dd;
    --blue-mist: #c9cbf3;
    --cream: #fdfdf4;
    --white: #ffffff;
    --ink: #111111;
    --grey: #6a6a6a;
  }
  * { margin: 0; padding: 0; box-sizing: border-box; }
  html, body {
    width: 1200px;
    height: 1000px;
    overflow: hidden;
    background: var(--backdrop);
  }
  .canvas {
    position: relative;
    width: 1200px;
    height: 1000px;
  }
  .card {
    position: absolute;
    left: 100px;
    top: 214px;
    width: 1000px;
    height: 572px;
    background: linear-gradient(90deg,
      var(--blue-deep) 0%,
      var(--blue-mist) 20%,
      var(--cream) 32%,
      var(--white) 56%,
      #e6e6fa 70%,
      var(--blue-soft) 86%,
      #8c8ce3 100%);
    box-shadow: 0 6px 18px rgba(0,0,0,0.25);
    font-family: "Archivo Black", "Arial Black", sans-serif;
    color: var(--ink);
  }
  .brand-mark {
    position: absolute;
    left: 150px;
    top: 98px;
    width: 46px;
    height: 46px;
    background: var(--blue-deep);
  }
  .brand-name {
    position: absolute;
    line-height: 1;
    color: var(--ink);
  }
  .brand-name--top { left: 330px; top: 30px; font-size: 64px; letter-spacing: 3px; }
  .brand-name--bottom { left: 215px; top: 108px; font-size: 74px; letter-spacing: 3px; }
  .tagline {
    position: absolute;
    left: 90px;
    top: 208px;
    font-family: "Cousine", "Courier New", monospace;
    font-style: italic;
    font-weight: 700;
    font-size: 25px;
    letter-spacing: 1px;
  }
  .person-name {
    position: absolute;
    left: 470px;
    top: 282px;
    font-size: 38px;
    letter-spacing: 4px;
  }
  .person-surname {
    position: absolute;
    left: 650px;
    top: 258px;
    font-size: 38px;
    letter-spacing: 4px;
  }
  .person-role {
    position: absolute;
    left: 660px;
    top: 312px;
    font-size: 30px;
    letter-spacing: 2px;
    color: var(--grey);
  }
  .contact {
    position: absolute;
    left: 100px;
    top: 412px;
    list-style: none;
    font-size: 26px;
    letter-spacing: 3px;
    line-height: 52px;
  }
  .contact-label {
    display: inline-block;
    width: 80px;
  }
</style>
</head>
<body>
<div class="canvas">
  <section class="card" aria-label="Brellow Gateworks business card">
    <span class="brand-mark" aria-hidden="true"></span>
    <div class="brand-name brand-name--top">Brellow</div>
    <div class="brand-name brand-name--bottom">Gateworks</div>
    <p class="tagline">install, service, repair &amp; automate garage doors</p>
    <div class="person-name">Glen</div>
    <div class="person-surname">???????</div>
    <div class="person-role">Proprietor</div>
    <ul class="contact">
      <li><span class="contact-label">T :</span>0412 638 905</li>
      <li><span class="contact-label">@ :</span>glen@brellow.com.au</li>
      <li>www.brellow.com.au</li>
    </ul>
  </section>
</div>
</body>
</html>
```